Seed Company Looking For a Soybean Seed Bag Design

We are are a regional seed company who is currently launching a new line of soybean products. The brand of the product will be Tru-Vora. We are looking for a custom design of a soybean bag measuring 16"x5"x30" (when constructed). We are looking for a modern design that's relatively loud, but not too busy. The proof needs to match with the attached template. We have also provided a proof of a previous bag project (Fox-Brook-Standard) we've done to show how the artwork needs to be laid out. In no way does the new design need to resemble the example. Also attached are some other examples of seed bags.
Agriculture
Designer to choose colors to be used in the design.

```html
<!DOCTYPE html>
<html lang="en">
<head>
<meta charset="utf-8">
<title>Tru-Vora Soybean Seed Bag – Dieline</title>
<link rel="stylesheet" href="https://fonts.googleapis.com/css2?family=Orbitron:wght@500;700;800&family=Saira+Stencil+One&display=swap">
<style>
  :root {
    --page: #ffffff;
    --bleed: #e6e6e7;
    --guide: #9fd3e8;
    --panel: #ffffff;
    --brand-green: #2f9b45;
    --art-green-soft: #e4f3e7;
    --art-green-faint: #f3faf4;
    --brand-grey: #646566;
    --banner-grey: #626364;
    --dim-blue: #2a8fd0;
  }
  * { margin: 0; padding: 0; box-sizing: border-box; }
  html, body { width: 1200px; height: 603px; overflow: hidden; background: var(--page); }
  .canvas { position: relative; width: 1200px; height: 603px; }

  .dieline { position: absolute; left: 181px; top: 0; width: 838px; height: 603px; background: var(--bleed); }
  .guide-v { position: absolute; top: 0; bottom: 0; border-left: 1px dashed var(--guide); }
  .guide-h { position: absolute; left: 0; right: 0; border-top: 1px dashed var(--guide); }

  .panel { position: absolute; top: 40px; height: 522px; background: var(--panel); overflow: hidden; }
  .panel--side-left { left: 44px; width: 92px; }
  .panel--front { left: 155px; width: 298px; }
  .panel--side-right { left: 474px; width: 92px; }
  .panel--back { left: 638px; width: 200px; }

  .accent-bar { position: absolute; left: 35px; top: 0; width: 8px; height: 90px; background: var(--brand-green); border-radius: 0 0 0 5px; }

  .tape-note { position: absolute; right: 4px; top: 4px; font: 700 5.5px "Orbitron", sans-serif; color: #333; border: 0.6px solid #333; padding: 1px 8px 1px 3px; letter-spacing: 0.2px; background: var(--panel); z-index: 2; }

  .wordmark { font-family: "Orbitron", sans-serif; font-weight: 800; letter-spacing: 2px; white-space: nowrap; }
  .tagline { font-family: "Orbitron", sans-serif; font-weight: 500; font-size: 6.4px; letter-spacing: 0.4px; color: var(--brand-grey); white-space: nowrap; }

  .sweep-art { position: absolute; left: 100px; top: 0; width: 198px; height: 340px; border-radius: 0 0 60% 100%; background: linear-gradient(160deg, var(--art-green-faint) 0%, var(--art-green-soft) 55%, var(--art-green-faint) 100%); }
  .seedling-art { position: absolute; left: 80px; top: 318px; width: 180px; height: 66px; border-radius: 60% 40% 50% 50%; background: radial-gradient(ellipse at 40% 60%, #d6eedb 0%, var(--art-green-soft) 55%, var(--art-green-faint) 100%); }

  .front-brand { position: absolute; left: 0; right: 0; top: 198px; text-align: center; z-index: 1; }
  .front-brand__mark { display: inline-block; width: 13px; height: 13px; background: var(--brand-grey); margin-right: 8px; vertical-align: 4px; }
  .front-brand .wordmark { display: inline-block; font-size: 26px; color: var(--brand-green); }
  .front-brand .tagline { margin-top: 8px; display: flex; align-items: center; justify-content: center; gap: 6px; }
  .front-brand .tagline::before, .front-brand .tagline::after { content: ""; width: 22px; border-top: 1px solid var(--brand-grey); }

  .product-banner { position: absolute; left: 35px; top: 392px; width: 222px; height: 82px; background: var(--banner-grey); border-radius: 0 40px 0 14px; text-align: center; color: #fff; font-family: "Saira Stencil One", sans-serif; z-index: 1; }
  .product-banner__line1 { display: block; font-size: 22px; letter-spacing: 2px; padding-top: 15px; line-height: 1; }
  .product-banner__line2 { display: block; font-size: 28px; letter-spacing: 10px; padding-left: 10px; margin-top: 2px; line-height: 1; }

  .side-brand { position: absolute; top: 158px; height: 206px; }
  .side-brand .wordmark, .side-brand .tagline { position: absolute; top: 0; height: 206px; writing-mode: vertical-rl; text-align: center; }
  .side-brand .wordmark { font-size: 30px; letter-spacing: 3px; line-height: 36px; }
  .side-brand .tagline { line-height: 10px; display: flex; align-items: center; justify-content: center; gap: 4px; }
  .side-brand .tagline::before, .side-brand .tagline::after { content: ""; height: 8px; border-left: 1px solid var(--brand-grey); }
  .side-brand--left .tagline { left: 4px; }
  .side-brand--left .wordmark { left: 20px; color: var(--brand-grey); }
  .side-brand--right .wordmark { left: 18px; color: var(--brand-green); }
  .side-brand--right .tagline { left: 60px; }

  .back-brand { position: absolute; left: 76px; top: 452px; font-family: "Orbitron", sans-serif; font-weight: 800; font-size: 7px; letter-spacing: 0.5px; color: var(--brand-green); }

  .dimension { position: absolute; top: 592px; font: 500 7px "Orbitron", sans-serif; color: #555; display: flex; align-items: center; gap: 4px; }
  .dimension::before { content: "\25C2"; color: var(--dim-blue); font-size: 8px; }
  .dimension::after { content: "\25B8"; color: var(--dim-blue); font-size: 8px; }
</style>
</head>
<body>
<div class="canvas">
  <div class="dieline">
    <div class="guide-h" style="top:40px"></div>
    <div class="guide-h" style="top:562px"></div>
    <div class="guide-v" style="left:38px"></div>
    <div class="guide-v" style="left:141px"></div>
    <div class="guide-v" style="left:459px"></div>
    <div class="guide-v" style="left:562px"></div>

    <section class="panel panel--side-left">
      <div class="side-brand side-brand--left">
        <span class="tagline">GROWING STRONG, PLANTING TOGETHER ALWAYS</span>
        <span class="wordmark">TRU-VORA</span>
      </div>
    </section>

    <section class="panel panel--front">
      <div class="sweep-art" role="img" aria-label="Decorative fine green lines sweeping down from the top of the bag toward the seedling"></div>
      <div class="seedling-art" role="img" aria-label="Line illustration of a sprouting soybean seedling with broad leaves"></div>
      <div class="accent-bar"></div>
      <div class="tape-note">EZ OPEN-PULL NARROW TAPE</div>
      <div class="front-brand">
        <span class="front-brand__mark"></span><span class="wordmark">TRU-VORA</span>
        <div class="tagline">GROWING STRONG, PLANTING TOGETHER ALWAYS</div>
      </div>
      <div class="product-banner">
        <span class="product-banner__line1">SOYBEAN</span>
        <span class="product-banner__line2">SEED</span>
      </div>
    </section>

    <section class="panel panel--side-right">
      <div class="side-brand side-brand--right">
        <span class="wordmark">TRU-VORA</span>
        <span class="tagline">GROWING STRONG, PLANTING TOGETHER ALWAYS</span>
      </div>
    </section>

    <section class="panel panel--back">
      <div class="back-brand">TRU-VORA</div>
    </section>

    <span class="dimension" style="left:80px">5"</span>
    <span class="dimension" style="left:294px">16"</span>
    <span class="dimension" style="left:508px">5"</span>
    <span class="dimension" style="left:724px">13"</span>
  </div>
</div>
</body>
</html>
```